Need Business Card for our Indian Grocery Store

Industry/Entity Type

Grocery Store

Contact Information for Business Card

Manoj Baweja
Director

Store Locations:

Thomastown
482 Elm Parade
P: 03 9172 5843

Reservoir
613 Carlow Road
P: 03 9238 6014

email: kvtmarts@mailnest.example

Requirements
Must have
• Our logo Colours

```html
<!DOCTYPE html>
<html lang="en">
<head>
<meta charset="utf-8">
<title>KVT Marts Business Card</title>
<link rel="stylesheet" href="https://fonts.googleapis.com/css2?family=Mulish:wght@400;700&display=swap">
<style>
  :root {
    --brand-red: #e31b23;
    --ink: #1a1a1a;
    --paper: #ffffff;
    --frame: #111111;
    --pattern-light: #f7c9cb;
  }
  * { margin: 0; padding: 0; box-sizing: border-box; }
  html, body {
    width: 1200px;
    height: 994px;
    overflow: hidden;
    background: var(--paper);
    font-family: "Mulish", sans-serif;
    color: var(--ink);
  }
  .canvas { position: relative; width: 1200px; height: 994px; }
  .card {
    position: absolute;
    top: 0;
    width: 565px;
    height: 994px;
    background: var(--paper);
    border: 2px solid var(--frame);
    overflow: hidden;
  }
  .card--front { left: 0; }
  .card--back { left: 636px; width: 564px; }
  .border-pattern {
    position: absolute;
    top: 0; left: 0;
    width: 120px;
    height: 100%;
    background: linear-gradient(90deg, var(--brand-red) 0%, var(--pattern-light) 45%, var(--brand-red) 55%, var(--pattern-light) 100%);
  }
  .brand {
    position: absolute;
    left: 153px;
    top: 120px;
    display: flex;
    align-items: center;
    gap: 14px;
    color: var(--brand-red);
    font-weight: 700;
    font-size: 46px;
    line-height: 1;
  }
  .brand__mark { width: 28px; height: 28px; background: var(--brand-red); }
  .person { position: absolute; left: 153px; top: 330px; font-size: 32px; line-height: 40px; }
  .person__name { color: var(--brand-red); font-weight: 700; }
  .email {
    position: absolute;
    left: 153px;
    top: 496px;
    font-size: 27px;
    white-space: nowrap;
  }
  .locations { position: absolute; left: 150px; top: 128px; font-size: 32px; }
  .locations__title { color: var(--brand-red); font-weight: 700; font-size: 32px; margin-bottom: 76px; }
  .store { line-height: 40px; margin-bottom: 68px; }
</style>
</head>
<body>
<div class="canvas">
  <section class="card card--front">
    <div class="border-pattern" role="img" aria-label="Red and white Indian paisley border pattern"></div>
    <div class="brand"><span class="brand__mark"></span><span class="brand__name">KVT Marts</span></div>
    <div class="person">
      <p class="person__name">Manoj Baweja</p>
      <p class="person__role">Director</p>
    </div>
    <p class="email">kvtmarts@mailnest.example</p>
  </section>

  <section class="card card--back">
    <div class="border-pattern" role="img" aria-label="Red and white Indian paisley border pattern"></div>
    <div class="locations">
      <h2 class="locations__title">Store Locations</h2>
      <div class="store">
        <p>Reservoir</p>
        <p>613 Carlow Road</p>
        <p>P: 03 9238 6014</p>
      </div>
      <div class="store">
        <p>Thomastown</p>
        <p>482 Elm Parade</p>
        <p>P: 03 9172 5843</p>
      </div>
    </div>
  </section>
</div>
</body>
</html>
```